NEED LABEL FOR PACKAGED DRINKING WATER BOTTLE

we are a new company who is into manufacturing of packaged drinking water bottles in 200 ml 500 ml and 1000 ml. we already have a label which we are using in our local market but we are introducing our 200ml bottle in inflight catering where our products will be seen, consumed by various age and origin of people who travel on flights. so we want a label which is simple and elegant.the bottle is a square bottle and label size would be 198 mm x 36 mm.you can use the label provided below for reference.and the bottle shape also is provided
Target Market(s)
flight passengers in domestic flights
Industry/Entity Type
It Company
Look and feel

```html
<!DOCTYPE html>
<html lang="en">
<head>
<meta charset="UTF-8">
<title>Serena Natural Mineral Water – 200 ml Label</title>
<link href="https://fonts.googleapis.com/css2?family=Open+Sans:wght@400;700&display=swap" rel="stylesheet">
<style>
  :root {
    --page-bg: #ecebea;
    --band-violet: #5b56c8;
    --band-blue: #4f9fe3;
    --band-sky: #8fd0f5;
    --band-mist: #eaf6fc;
    --band-white: #ffffff;
    --swoosh-violet: #4a3da6;
    --base-cyan: #3fb6ea;
    --base-cyan-light: #6fcdf3;
    --brand-ink: #5a4f96;
    --tagline-ink: #1f1f24;
  }
  * { margin: 0; padding: 0; box-sizing: border-box; }
  html, body {
    width: 1200px;
    height: 1000px;
    overflow: hidden;
    background: var(--page-bg);
  }
  .canvas {
    position: relative;
    width: 1200px;
    height: 1000px;
  }
  .label {
    position: absolute;
    left: 100px;
    top: 335px;
    width: 1000px;
    height: 330px;
    box-shadow: 0 10px 30px rgba(0,0,0,0.12);
  }
  .label-art {
    position: absolute;
    inset: 0;
    width: 100%;
    height: 100%;
    display: block;
  }
  .brand-name {
    position: absolute;
    left: 0;
    right: 0;
    top: 28px;
    text-align: center;
    font-family: "Open Sans", sans-serif;
    font-weight: 700;
    font-size: 128px;
    line-height: 1;
    letter-spacing: 2px;
    color: var(--brand-ink);
  }
  .tagline {
    position: absolute;
    left: 0;
    right: 0;
    top: 188px;
    text-align: center;
    font-family: "Open Sans", sans-serif;
    font-weight: 400;
    font-size: 36px;
    line-height: 1;
    color: var(--tagline-ink);
  }
</style>
</head>
<body>
<main class="canvas">
  <section class="label" aria-label="Bottle label">
    <svg class="label-art" viewBox="0 0 1000 330" preserveAspectRatio="none" aria-hidden="true">
      <defs>
        <linearGradient id="bodyGradient" x1="0" y1="0" x2="0" y2="1">
          <stop offset="0" stop-color="var(--band-violet)"/>
          <stop offset="0.09" stop-color="var(--band-blue)"/>
          <stop offset="0.3" stop-color="var(--band-sky)"/>
          <stop offset="0.52" stop-color="var(--band-mist)"/>
          <stop offset="0.6" stop-color="var(--band-white)"/>
        </linearGradient>
        <linearGradient id="baseGradient" x1="0" y1="0" x2="0" y2="1">
          <stop offset="0" stop-color="var(--base-cyan-light)"/>
          <stop offset="1" stop-color="var(--base-cyan)"/>
        </linearGradient>
      </defs>
      <rect class="label-body" x="0" y="0" width="1000" height="330" fill="url(#bodyGradient)"/>
      <path class="label-base" d="M0,262 Q520,252 1000,212 L1000,330 L0,330 Z" fill="url(#baseGradient)"/>
      <path class="label-swoosh" d="M0,252 Q520,242 1000,196 L1000,214 Q520,258 0,266 Z" fill="var(--swoosh-violet)"/>
    </svg>
    <h1 class="brand-name">serena</h1>
    <p class="tagline">Natural Mineral Water</p>
  </section>
</main>
</body>
</html>
```